Flyer für Beratung, Planung und Montage von Photovoltaikanlagen, Wallboxen usw.
Der Ablauf war optimal. Auf Änderungswünsche wurde umgehend eingegangen. Die Bearbeitung erfolgt sehr zeitnah. Wir sind sehr zufrieden und können TOLVERIKO nur empfehlen.
Zielgruppe
Individuelle Beratung, Planung und Montage von Photovoltaikanlagen, Wallboxen, Balkonkraftwerke, PowerToHeat, Stromspeicher etc., (Neuanlagen & Bestandsanlagen), Privat- & Firmenkunden
Aufgabenstellung
Qualitativ hochwertige Markenprodukte, Seriös, Modern, Regionaler Anbieter, Flyer für gezielte regionale Verteilung (Briefkasten)

```html
<!DOCTYPE html>
<html lang="de">
<head>
<meta charset="utf-8">
<title>Ammer Volt – Flyer</title>
<link href="https://fonts.googleapis.com/css2?family=Inter:wght@300;400;500;600;700&display=swap" rel="stylesheet">
<style>
  :root{
    --bg:#e9ebea;
    --paper:#ffffff;
    --ink:#1d2421;
    --muted:#4a524e;
    --green-light:#4fc266;
    --green-mid:#2e9e5b;
    --green-dark:#27864f;
    --accent:#39b54a;
    --photo-top:#6f8f86;
    --photo-mid:#3f7a6c;
    --photo-low:#a8a55e;
  }
  *{margin:0;padding:0;box-sizing:border-box}
  html,body{width:1200px;height:800px;overflow:hidden}
  body{background:var(--bg);font-family:"Inter",Arial,sans-serif;color:var(--ink);display:flex;align-items:center;justify-content:center}
  .flyer{position:relative;width:540px;height:764px;background:var(--paper);box-shadow:0 6px 24px rgba(0,0,0,.12);overflow:hidden}
  .hero{position:absolute;left:24px;top:24px;width:492px;height:400px;
    background:linear-gradient(160deg,var(--photo-top) 0%,var(--photo-mid) 45%,#4f8a66 70%,var(--photo-low) 100%)}
  .brand{position:absolute;left:60px;top:78px;color:#fff;font-weight:300;font-size:38px;letter-spacing:6px}
  .headline{position:absolute;left:60px;top:150px;color:#fff;font-weight:500;font-size:33px;line-height:1.15;letter-spacing:-.5px}
  .service{position:absolute;width:164px;color:#fff;padding:22px 16px;text-align:center}
  .service h3{font-size:14px;font-weight:600;margin-bottom:16px;line-height:1.25}
  .service p{font-size:8.5px;line-height:1.55;font-weight:400}
  .service--pv{left:24px;top:340px;height:216px;background:var(--green-light);padding-top:70px}
  .service--storage{left:188px;top:296px;height:180px;background:var(--green-mid);padding-top:52px}
  .service--charging{left:352px;top:252px;height:168px;background:var(--green-dark);padding-top:26px}
  .intro{position:absolute;left:60px;top:574px;width:440px}
  .intro h2{font-size:24px;font-weight:300;letter-spacing:-.3px;line-height:1.2;margin-bottom:10px}
  .intro h2 strong{color:var(--accent);font-weight:600}
  .intro p{font-size:11px;line-height:1.45;color:var(--muted)}
  .rule{position:absolute;left:60px;right:40px;top:690px;height:1px;background:var(--accent)}
  .contact{position:absolute;top:702px;font-size:9px;color:var(--muted);line-height:1.4}
  .contact-row{display:flex;align-items:flex-start;gap:8px}
  .contact-row + .contact-row{margin-top:6px}
  .contact svg{flex:none;margin-top:1px}
  .contact--phone{left:60px}
  .contact--phone strong{display:block;font-size:15px;color:var(--ink);font-weight:700}
  .contact--address{left:280px}
  .contact--web{left:400px}
</style>
</head>
<body>
  <article class="flyer">
    <div class="hero" role="img" aria-label="Solarmodule vor einem Himmel bei Sonnenuntergang"></div>
    <div class="brand">AMMER VOLT</div>
    <h1 class="headline">Ihr regionaler Anbieter<br>für erneuerbare Energien</h1>

    <section class="service service--pv">
      <h3>Photovoltaikanlagen</h3>
      <p>Egal ob Eigenheim mit oder ohne Bestandsanlage, Gewerbeimmobilie oder Freifläche. Wir finden gemeinsam die passende Lösung für Sie!</p>
    </section>
    <section class="service service--storage">
      <h3>Stromspeicher</h3>
      <p>Privat- oder Gewerbespeicher, DC oder AC gekoppelt, Notstrom- oder Ersatzstromfähigkeit, Lastspitzenkappung (Peak Shaving)</p>
    </section>
    <section class="service service--charging">
      <h3>Ladeinfrastruktur &amp; Elektromobilität</h3>
      <p>Egal ob Wallbox mit Überschussladen, oder mehrere mit intelligentem Lastmanagement, Ladepark oder Tiefgarage, gerne beraten wir Sie auch hierzu.</p>
    </section>

    <section class="intro">
      <h2>Wir sind Ihre <strong>regionalen</strong> Experten</h2>
      <p>Egal, ob Sie Privat- oder Gewerbekunde sind. Wir bieten passgenaue Lösungen und 360° Service für Ihre individuellen Bedürfnisse – und das sowohl für Neu- als auch Bestandsanlagen. Von der detaillierten Planung bis zur professionellen Installation und darüber hinaus.</p>
    </section>

    <div class="rule"></div>

    <div class="contact contact--phone">
      <div class="contact-row">
        <svg width="14" height="14" viewBox="0 0 24 24" fill="none" stroke="var(--accent)" stroke-width="2"><path d="M5 3h4l2 5-3 2a11 11 0 0 0 6 6l2-3 5 2v4a2 2 0 0 1-2 2A17 17 0 0 1 3 5a2 2 0 0 1 2-2z"/></svg>
        <div>Kontaktieren Sie uns:<strong>08 231 - 47 28 300</strong></div>
      </div>
    </div>
    <div class="contact contact--address">
      <div class="contact-row">
        <svg width="12" height="14" viewBox="0 0 24 28" fill="none" stroke="var(--accent)" stroke-width="2"><path d="M12 26s9-9 9-15a9 9 0 0 0-18 0c0 6 9 15 9 15z"/><circle cx="12" cy="11" r="3"/></svg>
        <div>Lindenweg 14B<br>86899 Kornau</div>
      </div>
    </div>
    <div class="contact contact--web">
      <div class="contact-row">
        <svg width="12" height="12" viewBox="0 0 24 24" fill="none" stroke="var(--accent)" stroke-width="2"><rect x="2" y="5" width="20" height="14" rx="2"/><path d="M2 7l10 7 10-7"/></svg>
        <div>info.ammervolt.de</div>
      </div>
      <div class="contact-row">
        <svg width="12" height="12" viewBox="0 0 24 24" fill="none" stroke="var(--accent)" stroke-width="2"><circle cx="12" cy="12" r="10"/><path d="M2 12h20M12 2c-5 6-5 14 0 20M12 2c5 6 5 14 0 20"/></svg>
        <div>www.ammervolt.de</div>
      </div>
    </div>
  </article>
</body>
</html>
```